Design some Stationery for Fieldwright, cards, letter heads and email footers

using the new logo design and bearing n mind the catalogue cover proof also attached (not not complete)

create the following:

Business card - logoname, title, address, mobile, ddi, main number, emaill address, main emaill address, web address standard size - unless you can do a distictive folding design.
Letter head: A4, logo, address, main email, main number. web address
Email footer - all of the above and DDi for the person.

some ideas: we want to print the reverse of the card and letter head, and the main email, tel no could go on the reverse of the cards.

one idea: is a logo wall paper to the reverse the inner cover on the catalogue will have one but we are struggling with how it will look so please do some good designs!

another is: solid black reverse with a tinted colour logo - large
another is: use of the grass and knife design from the catalogue cover....

re the mail footer: the knife design is one idea, we will need a reference to the special offers - please see here http://fieldwrightkit.example/bb.html? for a view of these.... in case you can use any design ideas from it.

Lets have your ideas please!

the company details are all attached with the logo files

****see layout sketch please****

```html
<!DOCTYPE html>
<html lang="en">
<head>
<meta charset="utf-8">
<title>Fieldwright business card</title>
<link rel="stylesheet" href="https://fonts.googleapis.com/css2?family=Open+Sans:wght@400;600;800&display=swap">
<style>
  :root {
    --page: #ecebe7;
    --card-dark: #2f2f31;
    --card-dark-edge: #242426;
    --card-light: #ffffff;
    --brand-green: #72b43c;
    --deep-green: #2f7a35;
    --brand-yellow: #f3d22a;
    --ink: #3a3a3a;
    --rule: #c9c9c9;
    --muted: #a9a9a9;
  }
  * { box-sizing: border-box; margin: 0; padding: 0; }
  html, body { width: 1200px; height: 900px; overflow: hidden; }
  body {
    background: var(--page);
    font-family: "Open Sans", Arial, sans-serif;
    display: flex;
    flex-direction: column;
    align-items: center;
    justify-content: center;
    gap: 50px;
  }
  .card {
    position: relative;
    width: 600px;
    height: 343px;
    border-radius: 4px;
    box-shadow: 0 6px 18px rgba(0,0,0,0.18);
    overflow: hidden;
  }

  /* Reverse side */
  .card-back {
    background: radial-gradient(ellipse at 50% 45%, #3c3c3e 0%, var(--card-dark) 55%, var(--card-dark-edge) 100%);
    display: flex;
    flex-direction: column;
    align-items: center;
    justify-content: center;
  }
  .card-back .wordmark { font-size: 44px; }
  .tagline {
    margin-top: 5px;
    font-size: 8px;
    letter-spacing: 3px;
    text-transform: uppercase;
    color: var(--muted);
  }
  .card-back .site {
    margin-top: 34px;
    font-size: 13px;
    color: #f2f2f2;
  }

  .wordmark {
    font-weight: 800;
    color: var(--brand-green);
    text-transform: uppercase;
    letter-spacing: -1px;
    line-height: 1;
  }

  /* Front side */
  .card-front { background: var(--card-light); }
  .card-front .wordmark {
    position: absolute;
    left: 30px;
    top: 92px;
    font-size: 46px;
  }
  .divider {
    position: absolute;
    left: 30px;
    right: 30px;
    top: 152px;
    border-top: 1px solid var(--rule);
  }
  .identity {
    position: absolute;
    left: 30px;
    top: 164px;
    font-size: 17px;
    color: var(--ink);
  }
  .identity .name { color: var(--brand-green); font-weight: 600; }
  .identity .bar { color: var(--brand-green); margin: 0 6px; }
  .identity .role { font-size: 14px; }
  .address {
    position: absolute;
    right: 30px;
    top: 104px;
    text-align: right;
    font-size: 13px;
    line-height: 1.45;
    color: var(--ink);
  }
  .contacts {
    position: absolute;
    left: 30px;
    top: 200px;
    list-style: none;
    font-size: 13.5px;
    color: var(--ink);
  }
  .contacts li {
    display: flex;
    align-items: center;
    gap: 10px;
    height: 22px;
  }
  .contacts svg { width: 14px; height: 14px; flex: none; }
  .bands {
    position: absolute;
    left: 0;
    bottom: 0;
    width: 600px;
    height: 343px;
  }
</style>
</head>
<body>

  <section class="card card-back" aria-label="Business card reverse">
    <div class="wordmark">Fieldwright</div>
    <div class="tagline">Tools &amp; Sundries Catalogue</div>
    <div class="site">www.fieldwright.example</div>
  </section>

  <section class="card card-front" aria-label="Business card front">
    <svg class="bands" viewBox="0 0 600 343" aria-hidden="true">
      <polygon points="0,296 372,296 362,312 0,312" fill="var(--brand-yellow)"/>
      <polygon points="382,296 600,296 600,312 372,312" fill="var(--deep-green)"/>
      <rect x="0" y="330" width="600" height="13" fill="var(--brand-yellow)"/>
    </svg>

    <div class="wordmark">Fieldwright</div>
    <div class="address">Unit 48, Marlow Bay,<br>Harlen County, United States</div>
    <div class="divider"></div>

    <div class="identity">
      <span class="name">Dana Whitfield</span><span class="bar">|</span><span class="role">CEO/President</span>
    </div>

    <ul class="contacts">
      <li>
        <svg viewBox="0 0 14 14" aria-hidden="true"><rect width="14" height="14" rx="3" fill="var(--brand-yellow)"/><path d="M4.5 3.5 L6 3.5 L6.6 5.5 L5.7 6.3 Q6.6 8 8 8.6 L8.7 7.7 L10.5 8.3 L10.5 9.8 Q7.5 10.2 5.4 7.8 Q3.8 5.8 4.5 3.5Z" fill="var(--ink)"/></svg>
        555.014.2290
      </li>
      <li>
        <svg viewBox="0 0 14 14" aria-hidden="true"><rect width="14" height="14" rx="3" fill="var(--brand-yellow)"/><rect x="3" y="4.5" width="8" height="5.5" fill="none" stroke="var(--ink)" stroke-width="1"/><path d="M3 4.5 L7 7.5 L11 4.5" fill="none" stroke="var(--ink)" stroke-width="1"/></svg>
        info@fieldwright.example
      </li>
      <li>
        <svg viewBox="0 0 14 14" aria-hidden="true"><rect width="14" height="14" rx="3" fill="var(--brand-yellow)"/><circle cx="7" cy="7" r="3.6" fill="none" stroke="var(--ink)" stroke-width="0.9"/><ellipse cx="7" cy="7" rx="1.5" ry="3.6" fill="none" stroke="var(--ink)" stroke-width="0.8"/><line x1="3.4" y1="7" x2="10.6" y2="7" stroke="var(--ink)" stroke-width="0.8"/></svg>
        www.fieldwright.example
      </li>
    </ul>
  </section>

</body>
</html>
```